Life Coaching Business Card

Please check out my website at www.lorettavisbeck.com. Ideally I would like to use the same colors that I used on the site to match my business cards i.e: pink, green, teal, white
I want the final design to include a picture of me and also to be appealing and eye catching. For the picture I submitted, you can crop it smaller to just have my face (exclude my chest) showing.
Industry/Entity Type
Business
Contact Information for Business Card
Loretta Visbeck
Transformational Life Coach
web: www.lorettavisbeck.com
email: loretta@lorettavisbeck.com
Phone: 555-318-7042
Look and feel
Each slider illustrates characteristics of the customer's brand and the style your logo design should communicate.

```html
<!DOCTYPE html>
<html lang="en">
<head>
<meta charset="utf-8">
<title>Loretta Visbeck – Transformational Life Coach Business Card</title>
<link rel="stylesheet" href="https://fonts.googleapis.com/css2?family=Arvo:ital,wght@0,400;0,700;1,400&family=Lato:wght@400;700&display=swap">
<style>
  :root {
    --lime: #a5cc35;
    --lime-text: #b3d93f;
    --pink: #e5197e;
    --pink-dark: #b0125f;
    --teal: #2bb1cb;
    --ink: #161616;
    --white: #ffffff;
    --silver-light: #f2f2f2;
    --silver-dark: #a9a9a9;
    --backdrop: #8f8f8f;
  }
  * { margin: 0; padding: 0; box-sizing: border-box; }
  html, body { width: 1200px; height: 1000px; overflow: hidden; }
  body {
    background: var(--backdrop);
    font-family: "Arvo", Georgia, serif;
    color: var(--ink);
    position: relative;
  }
  .card {
    position: absolute;
    left: 190px;
    width: 820px;
    height: 468px;
    overflow: hidden;
  }
  .card--back { top: 20px; background: var(--lime); }
  .card--front { top: 512px; background: #222; }

  /* Back side */
  .title-kicker {
    position: absolute; left: 40px; top: 22px;
    font-style: italic; font-size: 26px;
  }
  .title-main {
    position: absolute; left: 40px; top: 44px;
    font-size: 74px; letter-spacing: 2px; line-height: 1;
    font-weight: 400; z-index: 2;
  }
  .tagline-band {
    position: absolute; left: 0; top: 118px; width: 820px; height: 30px;
    background: linear-gradient(180deg, var(--silver-light), var(--silver-dark));
  }
  .tagline {
    position: absolute; left: 40px; top: 122px; z-index: 2;
    font-size: 17px;
  }
  .intro {
    position: absolute; left: 40px; top: 158px; width: 470px;
    font-size: 15px; line-height: 1.3;
  }
  .section-head {
    color: var(--pink); font-family: "Lato", sans-serif;
    font-size: 20px; letter-spacing: 1px; text-transform: uppercase;
  }
  .methods { position: absolute; left: 40px; top: 232px; }
  .methods ul { list-style: none; margin-top: 4px; }
  .methods li { font-size: 17px; line-height: 1.35; }
  .methods li::before { content: "▸"; margin-right: 4px; }

  .modes { position: absolute; left: 420px; top: 306px; }
  .mode { display: flex; align-items: center; gap: 10px; margin-bottom: 10px; }
  .mode-icon {
    width: 46px; height: 46px; border-radius: 9px; background: var(--ink);
    display: flex; align-items: center; justify-content: center;
  }
  .mode-label { font-size: 17px; line-height: 1.15; }

  .hours { position: absolute; left: 600px; top: 230px; width: 200px; }
  .hours-head { display: flex; align-items: center; gap: 10px; }
  .hours-head .section-head { line-height: 1.05; font-size: 19px; }
  .hours dl { margin-top: 8px; }
  .hours dt { font-size: 15px; }
  .hours dd {
    font-size: 17px; font-weight: 700; margin-bottom: 6px;
    padding-bottom: 3px; border-bottom: 1px dotted rgba(0,0,0,.4);
  }
  .hours dd::before { content: "▸ "; font-weight: 400; font-size: 13px; }

  /* Front side */
  .portrait {
    position: absolute; inset: 0;
    background: radial-gradient(ellipse at 40% 45%, #9a9a9a 0%, #5a5a5a 35%, #1e1e1e 75%);
  }
  .contact { position: absolute; left: 440px; top: 110px; color: var(--lime-text); }
  .contact-name { font-size: 30px; font-weight: 700; }
  .contact-line {
    font-family: "Lato", sans-serif; font-size: 22px;
    display: flex; align-items: center; gap: 8px; margin-top: 4px;
  }
  .social {
    position: absolute; left: 0; top: 196px; width: 350px; height: 116px;
    background: var(--teal); border-radius: 0 16px 16px 0;
    padding: 10px 16px; font-family: "Lato", sans-serif;
  }
  .social-head { font-family: "Arvo", serif; font-size: 20px; margin-bottom: 8px; }
  .social-grid {
    display: grid; grid-template-columns: auto auto; gap: 8px 16px;
    font-size: 14px; white-space: nowrap;
  }
  .social-item { display: flex; align-items: center; gap: 6px; }
  .social-item i { width: 12px; height: 12px; background: var(--ink); display: inline-block; flex: none; }
  .social-item b { font-weight: 700; }
  .sign-off {
    position: absolute; left: 30px; top: 336px;
    color: var(--pink); font-size: 26px; font-weight: 700; line-height: 1.15;
    text-transform: uppercase;
  }
  .ribbon { position: absolute; left: 410px; top: 236px; }
  .ribbon-text {
    position: absolute; left: 455px; top: 262px; width: 350px;
    color: var(--white); text-align: center;
  }
  .ribbon-question { font-family: "Lato", sans-serif; font-size: 15px; letter-spacing: .5px; line-height: 1.35; }
  .ribbon-url { font-family: "Lato", sans-serif; font-size: 23px; margin-top: 12px; }
  .ribbon-url b { font-weight: 700; }
</style>
</head>
<body>

<section class="card card--back" aria-label="Business card back">
  <p class="title-kicker">Transformational</p>
  <h1 class="title-main">LIFE COACH</h1>
  <div class="tagline-band"></div>
  <p class="tagline">Health, Strength &amp; Balance for Your Mind and Soul</p>
  <p class="intro">Specializing in couples and individuals experiencing disability in their lives; helping them discover a life without limits!</p>

  <div class="methods">
    <h2 class="section-head">Methodologies</h2>
    <ul>
      <li>Transformational Coaching Method</li>
      <li>Neuro Linguistic Programming</li>
      <li>Positive Psychology</li>
      <li>Ontological Coaching</li>
    </ul>
  </div>

  <div class="modes">
    <div class="mode">
      <span class="mode-icon">
        <svg width="26" height="26" viewBox="0 0 24 24" aria-hidden="true"><path fill="#fff" d="M6.6 10.8a15 15 0 0 0 6.6 6.6l2.2-2.2a1 1 0 0 1 1-.25 11.4 11.4 0 0 0 3.6.57 1 1 0 0 1 1 1V20a1 1 0 0 1-1 1A17 17 0 0 1 3 4a1 1 0 0 1 1-1h3.5a1 1 0 0 1 1 1c0 1.25.2 2.45.57 3.57a1 1 0 0 1-.25 1z"/></svg>
      </span>
      <span class="mode-label">Phone<br>Coaching</span>
    </div>
    <div class="mode">
      <span class="mode-icon">
        <svg width="28" height="20" viewBox="0 0 28 20" aria-hidden="true"><rect x="1" y="3" width="17" height="14" rx="3" fill="#fff"/><path fill="#fff" d="M19 8l8-5v14l-8-5z"/></svg>
      </span>
      <span class="mode-label">Online<br>Coaching</span>
    </div>
  </div>

  <div class="hours">
    <div class="hours-head">
      <svg width="40" height="40" viewBox="0 0 40 40" aria-hidden="true"><circle cx="20" cy="20" r="18" fill="#555"/><circle cx="20" cy="20" r="14" fill="#fff"/><path d="M20 10v10l6 4" stroke="#333" stroke-width="2" fill="none"/></svg>
      <h2 class="section-head">Coaching<br>Hours</h2>
    </div>
    <dl>
      <dt>Monday - Thursday</dt><dd>9:00am - 8:00pm</dd>
      <dt>Friday</dt><dd>9:00am - 6:00pm</dd>
      <dt>Saturday &amp; Sunday</dt><dd>9:00am - 4:00pm</dd>
    </dl>
  </div>
</section>

<section class="card card--front" aria-label="Business card front">
  <div class="portrait" role="img" aria-label="Black and white portrait photograph of the coach reclining on a leather sofa"></div>

  <div class="contact">
    <p class="contact-name">Loretta Visbeck</p>
    <p class="contact-line">
      <svg width="14" height="22" viewBox="0 0 14 22" aria-hidden="true"><rect x="1" y="1" width="12" height="20" rx="2" fill="none" stroke="currentColor" stroke-width="2"/></svg>
      555-318-7042
    </p>
    <p class="contact-line">
      <svg width="20" height="14" viewBox="0 0 20 14" aria-hidden="true"><rect width="20" height="14" fill="currentColor"/><path d="M0 0l10 8 10-8" stroke="#222" stroke-width="1.5" fill="none"/></svg>
      loretta@lorettavisbeck.com
    </p>
  </div>

  <div class="social">
    <p class="social-head">Follow me on:</p>
    <div class="social-grid">
      <span class="social-item"><i></i>Pagebook: Loretta Visbeck</span>
      <span class="social-item"><i></i>Chirper: <b>@lorvis</b></span>
      <span class="social-item"><i></i>Workline: Loretta Visbeck</span>
      <span class="social-item"><i></i>ClipTube: <b>lorvis</b></span>
    </div>
  </div>

  <p class="sign-off">Look forward<br>to working with you!</p>

  <svg class="ribbon" width="400" height="170" viewBox="0 0 400 170" aria-hidden="true">
    <polygon points="0,22 46,4 46,144 0,162 18,92" fill="var(--pink-dark)"/>
    <rect x="36" y="10" width="364" height="146" fill="var(--pink)"/>
  </svg>
  <div class="ribbon-text">
    <p class="ribbon-question">ARE YOU READY TO UP YOUR GAME<br>AND GET THE RESULTS THAT YOU WANT?</p>
    <p class="ribbon-url">www.<b>lorettavisbeck</b>.com</p>
  </div>
</section>

</body>
</html>
```